Beer Bottle Label

We are a boutique brewery. We need to design beer bottle labels. Our image theme so far has incorporated oil paintings from an Australian artist, and we would like to continue this theme. I will attach a demo label that I made (it's terrible!), and the image we would like to incorporate in the first design. I will also attach an image of the beer tap badge. We would like a label shaped like the demo I provide, or a rectangular label 8cm high * 15cm long. We are looking for a 'classy' label. The label also needs to incorporate our business logo, which I have attached. The Label must also include, in small writing: '4.5%abv' and 'contains approx. 1.2 standard drinks' and '330mL' and 'Brewed by Merriden Ales. 41 Pellow Road, Wattleford Victoria Australia 3391'.
If we receive an acceptable design from ArtHive, we would like you to design our other bottle labels, and redesign our beer tap badges.

Target Market(s)

Australian craft beer consumers

Industry/Entity Type

Boutique

Requirements
Must have
• Legal requirements: '4.5%abv' and 'contains approx. 1.2 standard drinks' and '330mL' and 'Brewed by Merriden Ales. 41 Pellow Road, Wattleford Victoria Australia 3391'
• Our business logo (see attached file).
• Must also utilise the painting (see attached file)

```html
<!DOCTYPE html>
<html lang="en">
<head>
<meta charset="utf-8">
<title>Redgum Draught – Bottle Label</title>
<link rel="stylesheet" href="https://fonts.googleapis.com/css2?family=Bebas+Neue&family=Cormorant+Garamond:ital,wght@0,500;0,600;1,500&family=Cormorant+SC:wght@600&family=Montserrat:wght@600&family=Mrs+Saint+Delafield&display=swap">
<style>
  :root {
    --page-bg: #f1f1f0;
    --paint-dark: #3d3420;
    --paint-olive: #6e6a3f;
    --paint-gold: #a8823d;
    --paint-mist: #a9ab94;
    --paint-rust: #7a4a22;
    --frame-gold: #b8913f;
    --frame-gold-light: #e6cf8e;
    --cartouche-white: #fbfbf9;
    --ink: #2a2520;
    --ink-soft: #4a4239;
    --label-text: #f4ecd8;
  }
  * { margin: 0; padding: 0; box-sizing: border-box; }
  html, body {
    width: 1200px; height: 1200px; overflow: hidden;
    background: var(--page-bg);
  }
  .canvas {
    position: relative; width: 1200px; height: 1200px;
    display: flex; align-items: center; justify-content: center;
  }
  .label {
    position: relative; width: 1040px; height: 556px;
    overflow: hidden;
    box-shadow: 0 10px 30px rgba(0,0,0,.18);
  }
  .label__painting {
    position: absolute; inset: 0;
    background:
      radial-gradient(ellipse at 20% 20%, rgba(190,192,170,.85), transparent 55%),
      radial-gradient(ellipse at 80% 15%, rgba(150,150,120,.7), transparent 50%),
      radial-gradient(ellipse at 30% 85%, rgba(168,130,61,.9), transparent 55%),
      radial-gradient(ellipse at 75% 75%, rgba(122,74,34,.75), transparent 55%),
      linear-gradient(180deg, var(--paint-mist) 0%, var(--paint-olive) 40%, var(--paint-gold) 70%, var(--paint-dark) 100%);
  }
  .label__shade {
    position: absolute; left: 0; right: 0; bottom: 0; height: 150px;
    background: linear-gradient(180deg, transparent, rgba(40,30,15,.55));
  }
  .cartouche {
    position: absolute; left: 50%; top: 96px;
    width: 370px; height: 326px; transform: translateX(-50%);
  }
  .cartouche svg { position: absolute; inset: 0; width: 100%; height: 100%; }
  .cartouche__content {
    position: absolute; inset: 0;
    display: flex; flex-direction: column; align-items: center;
    padding-top: 30px; color: var(--ink); text-align: center;
  }
  .brand-dot {
    width: 44px; height: 44px; border-radius: 50%;
    background: #3f6b3a;
  }
  .product-name {
    font-family: "Bebas Neue", sans-serif; font-weight: 400;
    font-size: 56px; line-height: .86; letter-spacing: 1px;
    margin-top: 20px; color: var(--ink);
  }
  .product-style {
    font-family: "Mrs Saint Delafield", cursive;
    font-size: 30px; line-height: 1; margin-top: 6px; color: var(--ink-soft);
  }
  .brewery-name {
    font-family: "Cormorant SC", serif; font-weight: 600;
    font-size: 22px; letter-spacing: 1.5px; margin-top: 6px; line-height: 1;
  }
  .brewery-sub {
    font-family: "Cormorant SC", serif; font-weight: 600;
    font-size: 10px; letter-spacing: 1px; margin-top: 4px; line-height: 1;
  }
  .brewery-place {
    font-family: "Cormorant SC", serif; font-weight: 600;
    font-size: 8px; letter-spacing: 1px; margin-top: 3px; line-height: 1; color: var(--ink-soft);
  }
  .legal {
    position: absolute; left: 0; right: 0; top: 450px;
    text-align: center; color: var(--label-text);
    text-shadow: 0 1px 2px rgba(0,0,0,.5);
  }
  .legal__abv {
    font-family: "Montserrat", sans-serif; font-weight: 600;
    font-size: 16px; letter-spacing: .5px;
  }
  .legal__drinks {
    font-family: "Cormorant SC", serif; font-weight: 600;
    font-size: 13px; letter-spacing: 1.5px; margin-top: 4px;
  }
  .legal__brewer {
    font-family: "Cormorant Garamond", serif; font-style: italic; font-weight: 500;
    font-size: 14px; margin-top: 2px;
  }
</style>
</head>
<body>
<main class="canvas">
  <section class="label">
    <div class="label__painting" role="img" aria-label="Australian oil painting: a settler on horseback beside a steam train in misty bushland, with a horse and gum trees"></div>
    <div class="label__shade"></div>

    <div class="cartouche">
      <svg viewBox="0 0 370 326" preserveAspectRatio="none" aria-hidden="true">
        <defs>
          <linearGradient id="goldEdge" x1="0" y1="0" x2="1" y2="1">
            <stop offset="0" stop-color="#e6cf8e"/>
            <stop offset=".45" stop-color="#b8913f"/>
            <stop offset=".7" stop-color="#e6cf8e"/>
            <stop offset="1" stop-color="#b8913f"/>
          </linearGradient>
        </defs>
        <path d="M60 8 H310 Q318 30 340 34 Q362 38 362 60 V266 Q362 288 340 292 Q318 296 310 318 H60 Q52 296 30 292 Q8 288 8 266 V60 Q8 38 30 34 Q52 30 60 8 Z"
              fill="#fbfbf9" stroke="url(#goldEdge)" stroke-width="9"/>
        <path d="M66 20 H304 Q312 40 334 44 Q350 48 350 64 V262 Q350 278 334 282 Q312 286 304 306 H66 Q58 286 36 282 Q20 278 20 262 V64 Q20 48 36 44 Q58 40 66 20 Z"
              fill="none" stroke="#b9b4a8" stroke-width="1.2" stroke-dasharray="2 3"/>
      </svg>
      <div class="cartouche__content">
        <div class="brand-dot"></div>
        <h1 class="product-name">Redgum<br>Draught</h1>
        <p class="product-style">craft beer</p>
        <p class="brewery-name">The Kestrel</p>
        <p class="brewery-sub">Brewery and Distillery</p>
        <p class="brewery-place">Wattleford, Victoria</p>
      </div>
    </div>

    <div class="legal">
      <p class="legal__abv">4.5% abv. 330ml</p>
      <p class="legal__drinks">Contains approx. 1.2 standard drinks</p>
      <p class="legal__brewer">Brewed by Merriden Ales. 41 Pellow Road, Wattleford Victoria Australia 3391</p>
    </div>
  </section>
</main>
</body>
</html>
```